Brin E's Jar Lable for kids Christmas gifts

Looking to get a wrap around label made for a quart canning jar. I would like it to have my kids head on it also. I was thinking in a silhouette form on both ends of the wrap( added a quick sketch up). We will be canning Pickles and giving them away as gifts this year. Also might be selling a few at a frames market. The brand name is " Brin E's" ( at the moment) So if you could think of a cool logo around that would be awesome also. I am an Orange and Black fan but I am up for suggestions also. Do you think this might be something you could help me with?

The second attached graphic is what I would like my kids faces to look similer to. Art wise. The sketch is of what the ends of the labels need to look like. Not a full face but a half of each of there faces on both ends of the lable.

Colors
f78f20
000000
757575

Requirements
Nice to have
• antique lable feel

```html
<!DOCTYPE html>
<html lang="en">
<head>
<meta charset="utf-8">
<title>Brin E's Jar Label</title>
<link rel="stylesheet" href="https://fonts.googleapis.com/css2?family=Oswald:wght@400;600&display=swap">
<style>
  :root {
    --canvas-bg: #e4e6e9;
    --label-black: #000000;
    --brand-orange: #f78f20;
    --brand-grey: #757575;
    --outline-white: #ffffff;
    --placeholder-dark: #3a3a3a;
  }
  html, body {
    margin: 0;
    padding: 0;
    width: 1200px;
    height: 1200px;
    overflow: hidden;
    background: var(--canvas-bg);
  }
  .canvas {
    position: relative;
    width: 1200px;
    height: 1200px;
  }
  .jar-label {
    position: absolute;
    left: 49px;
    top: 349px;
    width: 1101px;
    height: 550px;
    background: var(--label-black);
    overflow: hidden;
    font-family: "Oswald", "Arial Narrow", sans-serif;
    color: var(--brand-orange);
  }
  .photo-slot {
    position: absolute;
    top: 0;
    height: 550px;
  }
  .photo-slot--left { left: 0; width: 220px; }
  .photo-slot--right { right: 0; width: 190px; }

  .vertical-copy {
    position: absolute;
    left: 309px;
    top: 71px;
    height: 410px;
    display: flex;
    gap: 0;
  }
  .vertical-copy__line {
    writing-mode: vertical-rl;
    font-size: 23px;
    line-height: 29px;
    letter-spacing: 0.4px;
    white-space: nowrap;
  }

  .brand-frame {
    position: absolute;
    left: 555px;
    top: 54px;
    width: 290px;
    height: 178px;
    border: 2px dashed var(--outline-white);
    border-radius: 8px;
    box-sizing: border-box;
  }
  .brand-frame__inner {
    position: absolute;
    inset: 15px 16px;
    border: 2px dashed var(--outline-white);
    border-radius: 4px;
    display: flex;
    align-items: center;
    justify-content: center;
  }
  .brand-name {
    margin: 0;
    font-family: "Oswald", "Arial Narrow", sans-serif;
    font-weight: 600;
    font-size: 62px;
    line-height: 1;
    color: var(--brand-orange);
    white-space: nowrap;
  }

  .block-copy {
    position: absolute;
    left: 600px;
    top: 314px;
    margin: 0;
    font-size: 23px;
    line-height: 27.6px;
    letter-spacing: 0.4px;
  }
  .block-copy span { display: block; white-space: nowrap; }
</style>
</head>
<body>
<div class="canvas">
  <section class="jar-label">

    <svg class="photo-slot photo-slot--left" viewBox="0 0 220 550" role="img" aria-label="Photo placeholder: cut-out of the first child's face, left half">
      <defs>
        <linearGradient id="slotToneLeft" x1="0" y1="0" x2="0" y2="1">
          <stop offset="0" stop-color="var(--placeholder-dark)"/>
          <stop offset="1" stop-color="var(--brand-grey)"/>
        </linearGradient>
        <filter id="slotGlowLeft" x="-30%" y="-30%" width="160%" height="160%">
          <feGaussianBlur stdDeviation="7"/>
        </filter>
      </defs>
      <rect x="-60" y="36" width="255" height="474" rx="110"
            fill="none" stroke="var(--outline-white)" stroke-width="14" filter="url(#slotGlowLeft)" opacity="0.8"/>
      <rect x="-60" y="36" width="255" height="474" rx="110"
            fill="url(#slotToneLeft)" stroke="var(--outline-white)" stroke-width="6"/>
    </svg>

    <svg class="photo-slot photo-slot--right" viewBox="0 0 190 550" role="img" aria-label="Photo placeholder: cut-out of the second child's face, right half">
      <defs>
        <linearGradient id="slotToneRight" x1="0" y1="0" x2="0" y2="1">
          <stop offset="0" stop-color="var(--placeholder-dark)"/>
          <stop offset="1" stop-color="var(--brand-grey)"/>
        </linearGradient>
        <filter id="slotGlowRight" x="-30%" y="-30%" width="160%" height="160%">
          <feGaussianBlur stdDeviation="7"/>
        </filter>
      </defs>
      <rect x="28" y="78" width="230" height="428" rx="105"
            fill="none" stroke="var(--outline-white)" stroke-width="14" filter="url(#slotGlowRight)" opacity="0.8"/>
      <rect x="28" y="78" width="230" height="428" rx="105"
            fill="url(#slotToneRight)" stroke="var(--outline-white)" stroke-width="6"/>
    </svg>

    <div class="vertical-copy">
      <span class="vertical-copy__line">YOUR TEXT YOUR TEXT YOUR TEXT YOUR TEXT</span>
      <span class="vertical-copy__line">YOUR TEXT YOUR TEXT YOUR TEXT YOUR TEXT</span>
      <span class="vertical-copy__line">YOUR TEXT YOUR TEXT YOUR TEXT YOUR TEXT</span>
      <span class="vertical-copy__line">YOUR TEXT YOUR TEXT YOUR TEXT YOUR TEXT</span>
      <span class="vertical-copy__line">YOUR TEXT YOUR TEXT YOUR TEXT YOUR TEXT</span>
      <span class="vertical-copy__line">YOUR TEXT YOUR TEXT YOUR TEXT YOUR TEXT</span>
    </div>

    <div class="brand-frame">
      <div class="brand-frame__inner">
        <h1 class="brand-name">Brin E's</h1>
      </div>
    </div>

    <p class="block-copy">
      <span>YOUR TEXT YOUR TEXT</span>
      <span>YOUR TEXT YOUR TEXT</span>
      <span>YOUR TEXT YOUR TEXT</span>
      <span>YOUR TEXT YOUR TEXT</span>
      <span>YOUR TEXT YOUR TEXT</span>
      <span>YOUR TEXT YOUR TEXT</span>
    </p>

  </section>
</div>
</body>
</html>
```